Business card design needed for Renewable utilities company based in New Zealand.

We supply and install solar panels and all components along with it for a fully customisable PV system that helps customer save money on their energy bills right away and also save the planet!

I have attached logo & website design files to give you a better insight.

Business

```html
<!DOCTYPE html>
<html lang="en">
<head>
<meta charset="utf-8">
<title>Sunward Loop – Business Card</title>
<link rel="stylesheet" href="https://fonts.googleapis.com/css2?family=Questrial&family=Carlito:wght@400;700&display=swap">
<style>
  :root {
    --navy: #2a2f7e;
    --navy-deep: #1f2368;
    --navy-glow: #333d96;
    --sky: #1f86d0;
    --ink: #1d1f4f;
    --paper: #f4f4f4;
    --paper-edge: #d4d4d6;
    --stage: #e9e6e2;
    --white: #ffffff;
  }
  html, body {
    margin: 0;
    padding: 0;
    width: 1200px;
    height: 1181px;
    overflow: hidden;
    background: var(--stage);
  }
  .canvas {
    position: relative;
    width: 1200px;
    height: 1181px;
  }
  .card {
    position: absolute;
    left: 211px;
    width: 778px;
    border-radius: 28px;
    overflow: hidden;
  }
  /* Front */
  .card--front {
    top: 106px;
    height: 447px;
    background: radial-gradient(ellipse at 50% 45%, var(--navy-glow) 0%, var(--navy) 45%, var(--navy-deep) 100%);
  }
  .front__mark {
    position: absolute;
    left: 331px;
    top: 133px;
    width: 112px;
    height: 112px;
    border-radius: 50%;
    background: var(--white);
  }
  .front__name {
    position: absolute;
    left: 0;
    right: 0;
    top: 282px;
    text-align: center;
    font-family: "Questrial", sans-serif;
    font-size: 36px;
    letter-spacing: 0.5px;
    color: var(--white);
  }
  /* Back */
  .card--back {
    top: 618px;
    height: 445px;
    background: radial-gradient(ellipse at 45% 50%, var(--white) 0%, var(--paper) 40%, var(--paper-edge) 100%);
  }
  .back__band {
    position: absolute;
    left: 0;
    right: 0;
    background: var(--navy);
  }
  .back__band--top { top: 0; height: 52px; }
  .back__band--bottom { bottom: 0; height: 53px; }
  .back__mark {
    position: absolute;
    left: 184px;
    top: 140px;
    width: 134px;
    height: 134px;
    border-radius: 50%;
    background: linear-gradient(135deg, var(--sky) 0%, var(--navy) 100%);
  }
  .back__brand {
    position: absolute;
    left: 150px;
    width: 202px;
    top: 284px;
    text-align: center;
    font-family: "Questrial", sans-serif;
    font-size: 20px;
    color: var(--navy);
  }
  .back__divider {
    position: absolute;
    left: 388px;
    top: 150px;
    width: 2px;
    height: 147px;
    background: var(--navy);
  }
  .contact {
    position: absolute;
    left: 435px;
    top: 164px;
    font-family: "Carlito", sans-serif;
    color: var(--ink);
  }
  .contact__name {
    margin: 0;
    font-size: 25px;
    font-weight: 700;
    line-height: 1;
    color: var(--ink);
  }
  .contact__role {
    margin: 4px 0 0;
    font-size: 17px;
    font-weight: 700;
    color: var(--sky);
  }
  .contact__list {
    margin: 14px 0 0;
    padding: 0;
    list-style: none;
    font-size: 15px;
    font-weight: 700;
    line-height: 18px;
  }
  .contact__label {
    display: inline-block;
    width: 52px;
    color: var(--sky);
  }
</style>
</head>
<body>
<main class="canvas">
  <section class="card card--front" aria-label="Card front">
    <div class="front__mark" aria-hidden="true"></div>
    <div class="front__name">Sunward Loop</div>
  </section>

  <section class="card card--back" aria-label="Card back">
    <div class="back__band back__band--top"></div>
    <div class="back__mark" aria-hidden="true"></div>
    <div class="back__brand">Sunward Loop</div>
    <div class="back__divider"></div>
    <div class="contact">
      <p class="contact__name">YOUR NAME</p>
      <p class="contact__role">Managing Director</p>
      <ul class="contact__list">
        <li><span class="contact__label">Phone :</span>(555) 014-2280</li>
        <li><span class="contact__label">Email&nbsp;&nbsp;:</span>yourname@email.com</li>
        <li><span class="contact__label">Web&nbsp;&nbsp;&nbsp;&nbsp;:</span>www.yourweb.com</li>
      </ul>
    </div>
    <div class="back__band back__band--bottom"></div>
  </section>
</main>
</body>
</html>
```